Business Card Design for BrightHoppers Laser Tag Hire

We arrange fun and memorable laser tag birthday parties for 10-16yo kids.
The games are very active with lots of running, and are often held outdoors in nearby parks.
We aim to ensure that the kids really run around and have fun, whilst the parents relax and watch our crew set everything up, organise the kids and then run the games. Ideally the kids sleep really well that night!

The equipment is from Pellora Zingplay (many images online - some attached). We like the anime feel of mipo sky-crew and have included an action pic - thought it might be good to superimpose the zingplay kit plus a blaster in the hand of the character.
We do want to emphasise fun, healthy activity and the outdoors - so perhaps a park like background would be good!
I also like fully printed cards, with lines/images going right to the edge of the card.
Colours - like to keep orange as a key colour, eg the BrightHoppers company name.
Font - like Alexis for BrightHoppers - something futuristic but not too tacky.

Notes on Pictures - the cartoon character / Anime provided should not be used as is - only use the one of the boy running away - ideally this should be amended to have a sensor vest and blaster in the right hand.
The picture of the kids in the park - we dont really want this used, rather provided as a guide to the feeling we want to create.
Updates

Please see amendments to post - regarding pictures

1. The anime is an e.g., should be changed to incorp a sensor vest and blaster in hand to be really cool
2. The given pic of kids in the forest - not really our favourite pic, really just an eg of the feel we want to create, ie outdoors with kids (dont like as too many kids, too serious)
3. Random thought - how about incorporating the anime (with sensor and blaster in hand) in the foreground with a forest background. 
But I will leave it to you guys.
Thanks to those who have already submitted - I will send individualised feedback to you shortly.

Target Market(s)

Moms & Dads arranging parties / 10-16yo kids

Industry/Entity Type

Games

Contact Information for Business Card

BrightHoppers
Mobile Lasertag Hire for parties, school camps, club fundraisers, gala days
Owen 0437-614-209 Paula 0429-873-356
www.brighthoppers.com.au
bookings@brighthoppers.com.au

Requirements
Must have
• Very open mind
Nice to have
• brighter colours - would like a sense of the outdoors, with fun memories and healthy activity
Should not have
• not militaristic / serious
Dont normally like too dark with neon type look

```html
<!DOCTYPE html>
<html lang="en">
<head>
<meta charset="utf-8">
<title>BrightHoppers Business Card</title>
<link rel="stylesheet" href="https://fonts.googleapis.com/css2?family=Ubuntu:wght@400;500;700&family=Fira+Sans+Condensed:wght@700&display=swap">
<style>
  :root {
    --stage: #d6d6d6;
    --card-white: #ffffff;
    --ink-black: #151515;
    --brand-red: #e8372a;
    --panel-grey: #e4e5e5;
    --sky: #8cc8ee;
    --grass: #86c440;
    --text-dark: #1d1d1d;
  }
  html, body {
    margin: 0;
    width: 1200px;
    height: 926px;
    overflow: hidden;
    background: var(--stage);
  }
  .card {
    position: absolute;
    left: 100px;
    top: 177px;
    width: 1000px;
    height: 572px;
    background: var(--card-white);
    overflow: hidden;
    box-shadow: 0 10px 30px rgba(0,0,0,0.25);
    font-family: "Ubuntu", sans-serif;
  }
  .card-art {
    position: absolute;
    left: 0;
    top: 0;
    width: 1000px;
    height: 310px;
  }
  .brand-name {
    position: absolute;
    left: 44px;
    top: 98px;
    margin: 0;
    font-family: "Ubuntu", sans-serif;
    font-weight: 700;
    font-size: 40px;
    letter-spacing: 1px;
    text-transform: uppercase;
    color: var(--brand-red);
  }
  .tagline {
    position: absolute;
    left: 60px;
    top: 322px;
    margin: 0;
    font-family: "Fira Sans Condensed", sans-serif;
    font-weight: 700;
    font-size: 22px;
    letter-spacing: 0.6px;
    text-transform: uppercase;
    color: var(--text-dark);
  }
  .contact-band {
    position: absolute;
    left: 0;
    top: 372px;
    width: 1000px;
    height: 200px;
    background: var(--brand-red);
    color: var(--card-white);
  }
  .contact-list {
    list-style: none;
    margin: 0;
    padding: 0;
    position: absolute;
  }
  .contact-list li {
    display: flex;
    align-items: center;
    gap: 14px;
    font-size: 22px;
    margin-bottom: 16px;
  }
  .online-list { left: 50px; top: 28px; }
  .phone-list { right: 60px; top: 98px; }
  .phone-list li { font-size: 26px; margin-bottom: 18px; }
  .icon { width: 26px; height: 22px; flex: none; }
</style>
</head>
<body>
  <article class="card">
    <svg class="card-art" viewBox="0 0 1000 310" aria-hidden="false">
      <defs>
        <linearGradient id="park-scene" x1="0" y1="0" x2="0" y2="1">
          <stop offset="0" stop-color="var(--sky)"/>
          <stop offset="0.68" stop-color="#b9def5"/>
          <stop offset="0.72" stop-color="var(--grass)"/>
          <stop offset="1" stop-color="#7cbb38"/>
        </linearGradient>
      </defs>
      <rect width="1000" height="310" fill="var(--card-white)"/>
      <polygon class="grey-panel" points="860,0 1000,0 1000,310 860,310 935,155" fill="var(--panel-grey)"/>
      <polygon class="photo-window" role="img" aria-label="Action photo of a boy leaping across a park lawn wearing a sensor vest with a laser blaster"
        points="450,0 825,0 905,155 825,310 420,310 530,155" fill="url(#park-scene)"/>
      <polygon class="black-panel" points="0,0 425,0 505,150 395,310 0,310" fill="var(--ink-black)"/>
    </svg>
    <h1 class="brand-name">BrightHoppers</h1>
    <p class="tagline">Mobile Lasertag Hire for Parties, School Camps, Club Fundraisers, Gala Days</p>
    <section class="contact-band">
      <ul class="contact-list online-list">
        <li>
          <svg class="icon" viewBox="0 0 26 20"><rect x="1" y="1" width="24" height="18" fill="none" stroke="#fff" stroke-width="2"/><polyline points="1,1 13,11 25,1" fill="none" stroke="#fff" stroke-width="2"/></svg>
          bookings@brighthoppers.com.au
        </li>
        <li>
          <svg class="icon" viewBox="0 0 26 22"><rect x="1" y="1" width="24" height="15" fill="none" stroke="#fff" stroke-width="2"/><rect x="8" y="18" width="10" height="3" fill="#fff"/></svg>
          www.brighthoppers.com.au
        </li>
      </ul>
      <ul class="contact-list phone-list">
        <li>
          <svg class="icon" viewBox="0 0 26 22"><path d="M2 8 Q13 0 24 8 L21 11 L17 8 L9 8 L5 11 Z" fill="#fff"/><path d="M7 11 L19 11 L23 21 L3 21 Z" fill="#fff"/><circle cx="13" cy="16" r="2.5" fill="var(--brand-red)"/></svg>
          0437-614-209 (Owen)
        </li>
        <li>
          <svg class="icon" viewBox="0 0 26 22"><path d="M2 8 Q13 0 24 8 L21 11 L17 8 L9 8 L5 11 Z" fill="#fff"/><path d="M7 11 L19 11 L23 21 L3 21 Z" fill="#fff"/><circle cx="13" cy="16" r="2.5" fill="var(--brand-red)"/></svg>
          0429-873-356 (Paula)
        </li>
      </ul>
    </section>
  </article>
</body>
</html>
```